I need a newspaper ads that suits events / outings all over the world. refreshing feeling that suits my company logo.
Size of the ads is 6cm by 6cm a square
takenote
1) Joining up as members is free .
2) Places of interest tickets discount for members
3) Special events / outings host almost everyday
4) main point is everyone able to know each another
website : www.WandermoorHub.com
Target Market(s)
Targeting general age 18-40 . mainly singles
contents to put inside the ads
2) Local Places of interest tickets discount for members
4) Website : www.WandermoorHub.com
5) We also host photos contest
6) Meet the different faces of the world
7) Experience Sharing Gathering !
Industry/Entity Type
It Company
Requirements
Must have
- Refreshing feeling , and professional . will be uploading more pictures , kindly put some pictures combine into it to make people feel there is a lot activities can be involve when they join as member.

```html
<!DOCTYPE html>
<html lang="en">
<head>
<meta charset="utf-8">
<title>Wandermoor Events – Newspaper Ad</title>
<link rel="stylesheet" href="https://fonts.googleapis.com/css2?family=Arimo:wght@700&family=Roboto+Condensed:wght@500;700&display=swap">
<style>
  :root {
    --navy: #2e2552;
    --sky: #5aa7d8;
    --white: #ffffff;
    --orange: #f0861c;
    --lavender: #8c86c4;
    --green: #7dbb38;
    --cyan: #27b2e2;
    --amber: #f39c1f;
    --violet: #7d72b4;
    --leaf: #6cb43f;
    --yellow: #f5d21a;
    --photo-dark: #3b3a33;
    --photo-light: #8c9a6a;
  }
  * { box-sizing: border-box; margin: 0; padding: 0; }
  html, body { width: 1200px; height: 1200px; overflow: hidden; background: var(--white); }
  .ad {
    position: relative;
    width: 1200px;
    height: 1200px;
    background: var(--white);
    font-family: "Arimo", Arial, sans-serif;
  }
  .masthead {
    position: absolute;
    inset: 0 0 auto 0;
    height: 410px;
    background: var(--navy);
    text-align: center;
  }
  .brand {
    position: absolute;
    top: 40px;
    left: 0;
    right: 0;
    display: flex;
    flex-direction: column;
    align-items: center;
    gap: 16px;
  }
  .brand-mark {
    width: 104px;
    height: 104px;
    border-radius: 50%;
    background: var(--sky);
  }
  .brand-name {
    font-family: "Arimo", Arial, sans-serif;
    font-weight: 700;
    font-size: 38px;
    letter-spacing: 6px;
    color: var(--sky);
  }
  .headline {
    position: absolute;
    top: 268px;
    left: 0;
    right: 0;
    font-weight: 700;
    font-size: 55px;
    color: var(--white);
    letter-spacing: -0.5px;
  }
  .tagline {
    position: absolute;
    top: 340px;
    left: 0;
    right: 0;
    font-weight: 700;
    font-size: 55px;
    letter-spacing: -0.5px;
  }
  .tagline .experience { color: var(--orange); }
  .tagline .sharing { color: var(--lavender); }
  .tagline .gathering { color: var(--green); }

  .grid {
    position: absolute;
    top: 410px;
    left: 0;
    width: 1200px;
    height: 700px;
    display: grid;
    grid-template-columns: repeat(3, 1fr);
    grid-template-rows: repeat(3, 1fr);
  }
  .photo {
    background: linear-gradient(160deg, var(--photo-light) 0%, #6f7553 40%, var(--photo-dark) 100%);
  }
  .feature {
    display: flex;
    align-items: center;
    justify-content: center;
    text-align: center;
    padding: 0 24px;
    font-family: "Roboto Condensed", "Arial Narrow", sans-serif;
    font-weight: 500;
    font-size: 41px;
    line-height: 1.2;
    color: var(--white);
  }
  .feature--tickets { background: var(--cyan); }
  .feature--free { background: var(--amber); }
  .feature--events { background: var(--violet); }
  .feature--contest { background: var(--leaf); }

  .contact-bar {
    position: absolute;
    top: 1110px;
    left: 0;
    width: 1200px;
    height: 90px;
    border-top: 7px solid var(--yellow);
    background: var(--white);
    display: flex;
    align-items: center;
    justify-content: center;
    font-family: "Roboto Condensed", "Arial Narrow", sans-serif;
    font-weight: 700;
    font-size: 48px;
    letter-spacing: 2px;
    color: var(--navy);
    white-space: nowrap;
  }
</style>
</head>
<body>
  <main class="ad">
    <header class="masthead">
      <div class="brand">
        <span class="brand-mark" aria-hidden="true"></span>
        <span class="brand-name">WANDERMOOR EVENTS</span>
      </div>
      <h1 class="headline">Meet the different faces of the world</h1>
      <p class="tagline">
        <span class="experience">Experience</span>
        <span class="sharing">Sharing</span>
        <span class="gathering">Gathering !</span>
      </p>
    </header>

    <section class="grid">
      <div class="photo" role="img" aria-label="Group photo of young members smiling together at an outing"></div>
      <div class="feature feature--tickets">Local Places<br>of interest tickets<br>discount for members</div>
      <div class="photo" role="img" aria-label="Group photo of friends posing at a place of interest"></div>

      <div class="feature feature--free">Joining up as<br>members is free</div>
      <div class="photo" role="img" aria-label="Close group photo of members smiling at an event"></div>
      <div class="feature feature--events">Special events /<br>outings host almost<br>everyday</div>

      <div class="photo" role="img" aria-label="Group photo of members at an outing"></div>
      <div class="feature feature--contest">We also host<br>photos contest</div>
      <div class="photo" role="img" aria-label="Group photo of friends together at an attraction"></div>
    </section>

    <footer class="contact-bar">Call: 01987654320 | www.WandermoorHub.com</footer>
  </main>
</body>
</html>
```